We need a single page A4, single sided pdf brochure to promote our business to other businesses. Parcelo Back provides international returns solutions to on line retailers. This includes local return addresses and labels to allow customers to quickly and easily send their unwarted items back. we hen ship the returns back in bulk to the retailer.

```html
<!DOCTYPE html>
<html lang="en">
<head>
<meta charset="utf-8">
<title>Parcelo Back – International Returns Solutions</title>
<link rel="stylesheet" href="https://fonts.googleapis.com/css2?family=Bebas+Neue&family=Open+Sans:wght@400;700;800&family=Arimo:wght@400;700&display=swap">
<style>
  :root {
    --amber: #d9961e;
    --amber-text: #e08f1b;
    --ink: #1d1d1d;
    --panel: #1f1f1f;
    --white: #ffffff;
    --page-bg: #ecebe8;
    --body: #222222;
  }
  * { box-sizing: border-box; margin: 0; padding: 0; }
  html, body { width: 1200px; height: 1200px; overflow: hidden; background: var(--page-bg); }
  .flyer {
    position: absolute; left: 202px; top: 42px; width: 795px; height: 1116px;
    background: var(--white); overflow: hidden;
    box-shadow: 0 4px 18px rgba(0,0,0,.18);
    font-family: "Arimo", Arial, sans-serif; color: var(--body);
  }
  .backdrop { position: absolute; inset: 0; }
  .brand {
    position: absolute; left: 270px; top: 34px; display: flex; align-items: center; gap: 14px;
  }
  .brand-mark { width: 38px; height: 38px; background: var(--amber); }
  .brand-name {
    font-family: "Open Sans", sans-serif; font-weight: 800; font-size: 40px; line-height: 40px;
    color: var(--ink); letter-spacing: 1px; text-transform: uppercase;
  }
  .headline { position: absolute; left: 18px; top: 156px; font-family: "Bebas Neue", sans-serif; color: var(--ink); }
  .headline .kicker { font-size: 33px; line-height: 32px; letter-spacing: .2px; }
  .headline .main { font-size: 70px; line-height: 62px; }
  .intro { position: absolute; left: 25px; font-family: "Open Sans", sans-serif; font-weight: 700; color: var(--white); }
  .intro.lead { top: 260px; width: 430px; font-size: 16px; line-height: 22px; }
  .intro.sub { top: 313px; width: 400px; font-size: 12.5px; line-height: 17px; }
  .device-photo {
    position: absolute; left: 492px; top: 100px; width: 310px; height: 310px; border-radius: 50%;
    border: 5px solid var(--white);
    background: radial-gradient(circle at 55% 45%, #f4f4f4 0 30%, #2b2b2b 31% 45%, #d9b59a 46% 70%, #c89c80 100%);
  }
  .solution-box {
    position: absolute; left: 40px; top: 364px; width: 306px; height: 264px;
    background: var(--panel); border: 3px solid var(--white); border-radius: 6px; padding: 16px 18px 0 18px;
    box-shadow: 0 8px 10px -6px rgba(0,0,0,.35);
  }
  .solution-box h2 {
    font-family: "Bebas Neue", sans-serif; font-weight: 400; font-size: 29px; line-height: 30px;
    color: var(--amber-text); padding-bottom: 6px; border-bottom: 1px solid #bdbdbd; margin-bottom: 12px;
  }
  .solution-box ul { list-style: none; }
  .solution-box li {
    position: relative; padding-left: 12px; color: var(--white); font-size: 12.5px; line-height: 16px; margin-bottom: 15px;
  }
  .solution-box li::before { content: "•"; position: absolute; left: 0; }
  .solution-box .note { color: var(--white); font-size: 9.5px; line-height: 12px; margin-top: -4px; }
  .services { position: absolute; left: 364px; top: 450px; width: 420px; }
  .services h2 {
    font-family: "Open Sans", sans-serif; font-weight: 700; font-size: 21px; line-height: 23px; color: var(--amber-text);
    margin-bottom: 18px;
  }
  .services ul { list-style: none; }
  .services li {
    position: relative; padding-left: 12px; font-size: 12.5px; line-height: 15.5px; margin-bottom: 15.5px; color: var(--body);
  }
  .services li::before { content: "•"; position: absolute; left: 0; color: var(--amber-text); }
  .contact { position: absolute; left: 43px; top: 652px; width: 330px; }
  .contact h2 {
    font-family: "Open Sans", sans-serif; font-weight: 800; font-size: 36px; line-height: 44px;
    color: var(--amber-text); margin-left: 21px; margin-bottom: 6px;
  }
  .contact p { font-size: 13.5px; line-height: 16px; margin-bottom: 7px; }
  .contact .link { display: flex; align-items: center; gap: 9px; margin-left: 19px; font-weight: 700; font-size: 15px; }
  .contact .link svg { width: 17px; height: 17px; }
  .languages { display: flex; gap: 34px; margin-top: 16px; margin-left: -5px; }
  .languages svg { width: 28px; height: 28px; }
  .delivery-illustration {
    position: absolute; left: 352px; top: 672px; width: 436px; height: 408px;
    background: linear-gradient(135deg, #ffffff 0%, #f3f3f3 40%, #f7b36a 60%, #ee8a1e 80%, #ffffff 100%);
    opacity: .9;
  }
  .about-tab {
    position: absolute; left: 120px; top: 896px; width: 168px; height: 30px; background: var(--amber);
    border-radius: 10px 10px 0 0; text-align: center;
    font-family: "Open Sans", sans-serif; font-weight: 700; font-size: 20px; line-height: 32px; color: var(--white);
  }
  .about {
    position: absolute; left: 0; top: 924px; width: 438px; height: 158px; background: var(--panel);
    border-top-right-radius: 6px; padding: 8px 12px 0 24px; color: var(--white);
    font-size: 13.5px; line-height: 17px;
  }
  .about p { margin-bottom: 6px; }
  .footer-bar {
    position: absolute; left: 0; bottom: 0; width: 100%; height: 34px; background: var(--amber);
    display: flex; align-items: center; justify-content: center; gap: 8px;
    color: var(--white); font-size: 15.5px; letter-spacing: 2px;
  }
  .footer-bar svg { width: 18px; height: 18px; }
</style>
</head>
<body>
<main class="flyer">
  <svg class="backdrop" viewBox="0 0 795 1116" width="795" height="1116" aria-hidden="true">
    <path d="M0,112 C200,140 460,150 795,104 L795,440 C600,396 320,378 0,432 Z" fill="#d9961e"/>
  </svg>

  <div class="brand">
    <span class="brand-mark"></span>
    <span class="brand-name">Parcelo<br>Back</span>
  </div>

  <div class="headline">
    <div class="kicker">International Returns Solutions for</div>
    <div class="main">On-line Retailers</div>
  </div>
  <p class="intro lead">Selling internationally brings opportunities and challenges to retailers of all sizes.</p>
  <p class="intro sub">One of those challenges is how to deal effectively with customer returns.</p>

  <div class="device-photo" role="img" aria-label="Photo of a hand holding a smartphone showing an online shoe shop"></div>

  <section class="solution-box">
    <h2>Our Solution Includes :</h2>
    <ul>
      <li>LocalReturns Addresses in 9 Countries*</li>
      <li>Return Label solutions in over 20 other countries*</li>
      <li>Your own dedicated &amp; branded Label Portal</li>
      <li>Parcelo Back Retailer Portal to monitor and manage your returns</li>
    </ul>
    <p class="note">* Please see our website for an up-to-date list of countries we operate in.</p>
  </section>

  <section class="services">
    <h2>Parcelo Back have a range of services to suit retailers of all sizes that will :</h2>
    <ul>
      <li>Lower your returns costs – Save you and your customers money</li>
      <li>Improve your customers experience–Better feedback &amp; ratings</li>
      <li>Add value to your international business– More Sales</li>
      <li>Save time on managing International Returns – Less Administration</li>
      <li>Help you comply with marketplace International Return policies and best practice</li>
    </ul>
  </section>

  <div class="delivery-illustration" role="img" aria-label="Illustration of an orange courier figure handing a parcel to a figure at a door"></div>

  <section class="contact">
    <h2>Interested?</h2>
    <p>See our website for more information</p>
    <p class="link">
      <svg viewBox="0 0 20 20"><circle cx="10" cy="10" r="8.5" fill="none" stroke="#d9961e" stroke-width="1.5"/><ellipse cx="10" cy="10" rx="3.5" ry="8.5" fill="none" stroke="#d9961e" stroke-width="1.3"/><path d="M2 10h16M3.5 5.5h13M3.5 14.5h13" stroke="#d9961e" stroke-width="1.3"/></svg>
      www.parceloback.com
    </p>
    <p>or contact us to discuss how we can work together.</p>
    <p class="link">
      <svg viewBox="0 0 20 20"><rect x="1" y="4" width="18" height="12" fill="#d9961e"/><path d="M1 4l9 7 9-7M1 16l7-6M19 16l-7-6" fill="none" stroke="#fff" stroke-width="1.3"/></svg>
      info@parceloback.com
    </p>
    <p>Write to us in these languages</p>
    <div class="languages">
      <svg viewBox="0 0 30 30"><circle cx="15" cy="15" r="13" fill="#1f3f8f" stroke="#222" stroke-width="2"/><path d="M3 15h24M15 3v24" stroke="#fff" stroke-width="5"/><path d="M3 15h24M15 3v24" stroke="#c8102e" stroke-width="3"/></svg>
      <svg viewBox="0 0 30 30"><clipPath id="c2"><circle cx="15" cy="15" r="13"/></clipPath><g clip-path="url(#c2)"><rect x="0" y="0" width="30" height="11" fill="#111"/><rect x="0" y="11" width="30" height="8" fill="#dd0000"/><rect x="0" y="19" width="30" height="11" fill="#ffce00"/></g><circle cx="15" cy="15" r="13" fill="none" stroke="#222" stroke-width="2"/></svg>
      <svg viewBox="0 0 30 30"><clipPath id="c3"><circle cx="15" cy="15" r="13"/></clipPath><g clip-path="url(#c3)"><rect x="0" y="0" width="11" height="30" fill="#0055a4"/><rect x="11" y="0" width="8" height="30" fill="#fff"/><rect x="19" y="0" width="11" height="30" fill="#ef4135"/></g><circle cx="15" cy="15" r="13" fill="none" stroke="#222" stroke-width="2"/></svg>
      <svg viewBox="0 0 30 30"><clipPath id="c4"><circle cx="15" cy="15" r="13"/></clipPath><g clip-path="url(#c4)"><rect x="0" y="0" width="11" height="30" fill="#009246"/><rect x="11" y="0" width="8" height="30" fill="#fff"/><rect x="19" y="0" width="11" height="30" fill="#ce2b37"/></g><circle cx="15" cy="15" r="13" fill="none" stroke="#222" stroke-width="2"/></svg>
      <svg viewBox="0 0 30 30"><clipPath id="c5"><circle cx="15" cy="15" r="13"/></clipPath><g clip-path="url(#c5)"><rect x="0" y="0" width="30" height="30" fill="#c60b1e"/><rect x="0" y="9" width="30" height="12" fill="#ffc400"/></g><circle cx="15" cy="15" r="13" fill="none" stroke="#222" stroke-width="2"/></svg>
    </div>
  </section>

  <div class="about-tab">About Us</div>
  <section class="about">
    <p>Parcelo Back is a fast growing family-run business that has been providing International return services to on line sellers since 2015. Through our UK and French based businesses, together with our trusted partner network, we deliver a service that saves retailers money and time.</p>
    <p>The owners of Parcelo Back come from a retail and e-commerce background, so we fully understand and appreciate the issues and challenges faced by retailers and their customers.</p>
  </section>

  <footer class="footer-bar">
    <span>Call us @</span>
    <svg viewBox="0 0 20 20"><circle cx="10" cy="10" r="8.5" fill="none" stroke="#fff" stroke-width="1.5"/><path d="M7 5.5l1.6 2.4-1 1.2c.6 1.3 1.5 2.2 2.8 2.8l1.2-1 2.4 1.6-.8 1.8c-3.8-.3-6.7-3.2-7-7z" fill="#fff"/></svg>
    <span>+44(0)161 000 4821</span>
  </footer>
</main>
</body>
</html>
```